Website design for a construction company

The logo and the copies of all the 3 pages are attached below. I don't have a preference in colors but I would ideally like to use the colors on my logo, dark teal (secondary) and copper (primary).

Company Name: Torvin Group

Location: London, UK

Business Overview:

Torvin Group is a comprehensive construction company based in London, specializing in a wide range of construction services. We cater to various sectors, providing services including electrical work, painting and decorating, plastering, plumbing, carpentry, kitchen and bathroom installations, loft conversions, and extensions. Our team is known for its skilled craftsmanship, attention to detail, and commitment to quality.

What "TORVIN" stands for:

Our company name, 'TORVIN', is derived from Hephaestus, the ancient Greek god of craftsmen, blacksmiths, artisans, sculptors, metals, metallurgy, fire, and volcanoes. Hephaestus was renowned in mythology for his incredible skill in crafting and creating, making him the patron of all craftsmen and artisans. His name is synonymous with the mastery of artisanship and the creation of wondrous, enduring works.

In choosing 'TORVIN' as our name, we embody the spirit and skills of Hephaestus. It reflects our commitment to craftsmanship, excellence, and durability in the field of construction. Just as Hephaestus was known for his meticulous work, precision, and innovative creations, our company strives to uphold these qualities in every project we undertake.

Our name is a constant reminder of our dedication to quality, innovation, and the art of building. It symbolizes our endeavor to achieve the highest standards in construction, much like Hephaestus did in his timeless creations. In essence, 'TORVIN' is not just our name; it's a representation of our ethos and the high standards we set for ourselves in the construction industry.

Target Audience:

Our primary audience includes homeowners, real estate developers, and commercial clients in London seeking reliable, high-quality construction services.

Unique Selling Points:

Diverse Range of Services: Offering a one-stop solution for all construction needs.

Certified and Experienced: Professional team with a strong focus on delivering certified and compliant work, particularly in electrical services.

Client-Centric Approach: Emphasizing client satisfaction, we tailor our services to meet the unique needs and visions of our clients.

Quality and Reliability: Commitment to high-quality materials, skilled workmanship, and delivering projects on time and within budget.

Website Requirements:

Clean, professional design reflecting the quality and reliability of our services.

User-friendly navigation to easily access information about our services, portfolio, company background, and contact details.

Portfolio section showcasing our past projects with placeholders for images and descriptions.

Integration of a contact form, map for our location, and links to our social media accounts.

Mobile-responsive design to ensure accessibility across various devices.

Purpose of the Website:
The website aims to:

Establish an online presence and credibility in the construction industry.

Provide an informative resource about our services and past projects to potential clients.

Facilitate easy communication and inquiries through an integrated contact system.

Tone and Style:

Professional, informative, and welcoming. The website should convey trustworthiness and expertise in the construction field.

homeowners, real estate developers, and commercial clients

Construction

3 page

```html
<!DOCTYPE html>
<html lang="en">
<head>
<meta charset="utf-8">
<title>Torvin Group — Construction in London</title>
<link href="https://fonts.googleapis.com/css2?family=Oswald:wght@500;600;700&family=Open+Sans:wght@400;600;700&display=swap" rel="stylesheet">
<style>
:root{
  --teal:#1a8a80;
  --teal-dark:#0e5e58;
  --copper:#b08350;
  --copper-dark:#8a6336;
  --ink:#1e1e1e;
  --text:#555;
  --light:#f1f2f2;
  --footer:#1b1c1c;
  --white:#fff;
}
*{margin:0;padding:0;box-sizing:border-box}
html,body{width:1200px;height:3448px;overflow:hidden}
body{font-family:"Open Sans",Arial,sans-serif;color:var(--ink);background:var(--white);position:relative}
h1,h2,h3,.brand{font-family:"Oswald","Arial Narrow",sans-serif}
a{color:inherit;text-decoration:none}

.topbar{height:36px;background:var(--teal-dark);color:var(--white);display:flex;align-items:center;justify-content:space-between;padding:0 110px;font-size:14px}
.topbar .right{display:flex;align-items:center;gap:22px}
.dot{width:16px;height:16px;border-radius:50%;background:rgba(255,255,255,.85);display:inline-block}
.topbar .social{display:flex;gap:12px}

.nav{height:64px;background:var(--white);display:flex;align-items:center;padding-left:110px;position:relative;box-shadow:0 2px 6px rgba(0,0,0,.08);z-index:2}
.nav ul{list-style:none;display:flex;gap:44px;font-size:15px;font-weight:600}
.nav .left{flex:1}
.nav .right{display:flex;align-items:center;gap:40px}
.nav .logo{position:absolute;left:50%;transform:translateX(-50%);display:flex;align-items:center;gap:10px}
.logo .mark{width:34px;height:34px;background:var(--teal)}
.logo .brand{font-size:28px;font-weight:600;color:var(--teal-dark);letter-spacing:2px}
.quote-btn{background:var(--teal);color:var(--white);height:64px;padding:0 30px;display:flex;align-items:center;font-weight:700;font-size:15px}

.hero{height:660px;position:relative;background:linear-gradient(180deg,#8d8a85 0%,#c9c3b8 45%,#6b6862 100%);color:var(--white);text-align:center}
.hero .shade{position:absolute;inset:0;background:rgba(0,0,0,.35)}
.hero .inner{position:relative;padding-top:180px}
.hero h1{font-size:62px;font-weight:600;line-height:1.12;letter-spacing:1px}
.hero p{font-size:21px;font-weight:700;margin-top:10px}
.btn{display:inline-block;background:var(--teal);color:var(--white);font-weight:700;font-size:15px;padding:14px 30px;border-radius:4px}
.hero .btn{margin-top:30px}

.welcome{height:260px;text-align:center;position:relative}
.welcome .badge{position:absolute;left:50%;top:-46px;transform:translateX(-50%);width:92px;height:92px;background:var(--white);display:flex;align-items:center;justify-content:center;border-radius:50%}
.welcome .badge span{width:56px;height:56px;background:var(--teal)}
.welcome h2{font-size:46px;font-weight:600;padding-top:68px}
.welcome p{width:960px;margin:22px auto 0;font-size:16px;line-height:1.65;color:var(--text)}

.why{height:480px;background:var(--light);text-align:center}
.why h2{font-size:46px;font-weight:600;padding-top:42px}
.features{display:flex;justify-content:center;gap:80px;margin-top:44px}
.feature{width:290px}
.feature svg{display:block;margin:0 auto}
.feature h3{font-family:"Open Sans",sans-serif;font-size:20px;font-weight:700;margin:18px 0 14px}
.feature p{font-size:15px;line-height:1.7;color:var(--text);text-align:justify}

.services{height:740px;position:relative;color:var(--white);text-align:center}
.services svg.bg{position:absolute;inset:0}
.services .content{position:relative}
.services h2{font-size:50px;font-weight:600;padding-top:78px}
.services .lead{width:720px;margin:8px auto 0;font-size:16px;line-height:1.6}
.svc-label{font-family:"Open Sans",Arial,sans-serif;font-weight:700;font-size:17px;fill:#fff}

.clients{height:520px;text-align:center;position:relative}
.clients h2{font-size:50px;font-weight:600;padding-top:44px}
.clients .lead{width:700px;margin:10px auto 0;font-size:16px;line-height:1.6;color:var(--text)}
.cards{display:flex;justify-content:center;gap:60px;margin-top:36px}
.card{width:420px;height:180px;background:var(--white);box-shadow:0 3px 14px rgba(0,0,0,.14);border-radius:8px;display:flex;gap:26px;padding:34px 28px;text-align:left}
.avatar{width:92px;height:92px;border-radius:50%;background:linear-gradient(135deg,#c9b8a3,#7d6f62);flex:none}
.card p{font-size:14px;line-height:1.6;color:#777}
.card .name{font-weight:700;font-size:16px;color:var(--ink);margin-top:10px}
.stars{color:#e3a21a;font-size:16px;letter-spacing:2px}
.arrow{position:absolute;top:300px;font-size:34px;color:#777}

.cta{height:320px;background:linear-gradient(180deg,#b48a58,#8f6a3e);color:var(--white);text-align:center}
.cta h2{font-size:46px;font-weight:600;padding-top:72px}
.cta p{width:720px;margin:14px auto 0;font-size:16px;line-height:1.7}
.cta .btn{margin-top:26px}

.footer{height:368px;background:var(--footer);color:#ccc;position:relative;padding:60px 110px 0;display:flex}
.footer .about{width:370px}
.footer .logo{display:flex;align-items:center;gap:10px}
.footer .logo .brand{color:var(--white)}
.footer .social{display:flex;gap:12px;margin-top:24px;padding-left:10px}
.footer .social .dot{width:30px;height:30px;background:none;border:2px solid #ddd}
.footer .col{width:230px}
.footer h4{color:var(--white);font-size:17px;margin-bottom:14px}
.footer li{list-style:none;font-size:14px;line-height:1.9}
.contact-item{display:flex;gap:12px;margin-bottom:14px;font-size:14px}
.contact-item b{color:var(--white);display:block}
.copyright{position:absolute;left:0;right:0;bottom:0;height:58px;border-top:1px solid #333;text-align:center;line-height:58px;font-size:14px}
.to-top{position:absolute;right:50px;bottom:74px;width:40px;height:40px;border-radius:50%;background:var(--copper);color:var(--white);text-align:center;line-height:40px;font-weight:700}
</style>
</head>
<body>

<div class="topbar">
  <span>&#9742; +44 20 5550 1482</span>
  <div class="right">
    <span>&#9993; info@torvingroup.com</span>
    <div class="social"><span class="dot"></span><span class="dot"></span><span class="dot"></span></div>
  </div>
</div>

<nav class="nav">
  <ul class="left"><li>Home</li><li>About Us</li><li>Services</li></ul>
  <a class="logo" href="#"><span class="mark"></span><span class="brand">TORVIN</span></a>
  <div class="right">
    <ul><li>Projects</li><li>Contact Us</li></ul>
    <a class="quote-btn" href="#">GET A QUOTE</a>
  </div>
</nav>

<section class="hero" role="img" aria-label="Bright modern kitchen interior with white cabinets, marble counters and pendant lights">
  <div class="shade"></div>
  <div class="inner">
    <h1>BUILDING YOUR DREAMS<br>INTO REALITY</h1>
    <p>Expert Craftsmanship Meets Unmatched Reliability in the Heart of London</p>
    <a class="btn" href="#">GET STARTED &#10140;</a>
  </div>
</section>

<section class="welcome">
  <div class="badge"><span></span></div>
  <h2>WELCOME TO TORVIN GROUP</h2>
  <p>Where Construction Meets Excellence: Based in London, we are committed to transforming any space into exceptional places. Our team is dedicated to delivering the highest quality in every project, attending to every detail with precision and care.</p>
</section>

<section class="why">
  <h2>WHY CHOOSE US</h2>
  <div class="features">
    <div class="feature">
      <svg width="80" height="86" viewBox="0 0 80 86"><polygon points="40,2 77,23 77,63 40,84 3,63 3,23" fill="var(--teal)"/><circle cx="40" cy="43" r="14" fill="none" stroke="#fff" stroke-width="4"/></svg>
      <h3>Our Expertise</h3>
      <p>Leveraging over 10 years of experience, Torvin Group stands as a beacon of excellence in the construction industry. We handle each project, big or small, with unmatched professionalism and skill.</p>
    </div>
    <div class="feature">
      <svg width="80" height="86" viewBox="0 0 80 86"><polygon points="40,2 77,23 77,63 40,84 3,63 3,23" fill="var(--teal)"/><path d="M28 44l8 8 16-18" fill="none" stroke="#fff" stroke-width="5"/></svg>
      <h3>Quality Assurance</h3>
      <p>Quality is not just a promise, but a practice. Meticulous attention to detail ensures flawless finishes and durable structures, bringing long-lasting satisfaction to our clients.</p>
    </div>
    <div class="feature">
      <svg width="80" height="86" viewBox="0 0 80 86"><polygon points="40,2 77,23 77,63 40,84 3,63 3,23" fill="var(--teal)"/><circle cx="40" cy="38" r="11" fill="#fff"/><path d="M33 47l-4 14 11-5 11 5-4-14" fill="#fff"/></svg>
      <h3>Certified Excellence</h3>
      <p>Your safety and satisfaction are our top priorities. We provide electrical certificates and adhere to the highest industry standards, offering peace of mind in every service.</p>
    </div>
  </div>
</section>

<section class="services">
  <svg class="bg" width="1200" height="740" viewBox="0 0 1200 740">
    <defs><linearGradient id="svcGrad" x1="0" y1="0" x2="0" y2="1"><stop offset="0" stop-color="#1f958a"/><stop offset="1" stop-color="#0e5e58"/></linearGradient></defs>
    <path d="M0 40 Q600 -30 1200 40 V740 H0Z" fill="url(#svcGrad)"/>
    <path d="M261 630 A340 340 0 0 1 939 630" fill="none" stroke="rgba(255,255,255,.7)" stroke-width="3"/>
    <path d="M420 740 A180 180 0 0 1 780 740Z" fill="#e9f1f0"/>
    <circle cx="600" cy="610" r="96" fill="#fff"/>
    <text x="600" y="624" text-anchor="middle" font-family="Oswald, sans-serif" font-size="34" font-weight="600" fill="#0e5e58">TORVIN</text>

    <g stroke="rgba(255,255,255,.85)" stroke-width="2">
      <line x1="325" y1="337" x2="465" y2="337"/>
      <line x1="133" y1="407" x2="343" y2="407"/>
      <line x1="169" y1="511" x2="264" y2="511"/>
      <line x1="141" y1="630" x2="231" y2="630"/>
      <line x1="735" y1="337" x2="875" y2="337"/>
      <line x1="857" y1="407" x2="1150" y2="407"/>
      <line x1="936" y1="511" x2="1036" y2="511"/>
      <line x1="969" y1="630" x2="1059" y2="630"/>
    </g>

    <text class="svc-label" x="455" y="327" text-anchor="end">Electrical Work</text>
    <text class="svc-label" x="333" y="397" text-anchor="end">Painting and Decorating</text>
    <text class="svc-label" x="254" y="501" text-anchor="end">Plastering</text>
    <text class="svc-label" x="221" y="620" text-anchor="end">Plumbing</text>
    <text class="svc-label" x="745" y="327">Loft Conversions</text>
    <text class="svc-label" x="867" y="397">Kitchen and Bathroom Installations</text>
    <text class="svc-label" x="946" y="501">Extensions</text>
    <text class="svc-label" x="979" y="620">Carpentry</text>

    <g fill="#fff">
      <circle cx="495" cy="337" r="30"/><circle cx="373" cy="407" r="30"/><circle cx="294" cy="511" r="30"/><circle cx="261" cy="630" r="30"/>
      <circle cx="705" cy="337" r="30"/><circle cx="827" cy="407" r="30"/><circle cx="906" cy="511" r="30"/><circle cx="939" cy="630" r="30"/>
    </g>
    <g fill="none" stroke="#0e5e58" stroke-width="3">
      <path d="M499 323l-10 14h10l-8 14"/>
      <rect x="361" y="395" width="24" height="24"/>
      <rect x="282" y="500" width="24" height="12"/><path d="M294 512v12"/>
      <path d="M251 640l20-20M253 622l8 8"/>
      <path d="M695 347h20v-20h-20zM705 327v-6"/>
      <rect x="815" y="395" width="24" height="24"/>
      <path d="M894 523h24v-24M894 511h12"/>
      <path d="M929 640l20-20M931 622l16 16"/>
    </g>
  </svg>
  <div class="content">
    <h2>OUR SERVICES</h2>
    <p class="lead">Discover how we can bring your vision to life, covering every aspect of construction from the initial design to the final touches.</p>
  </div>
</section>

<section class="clients">
  <h2>OUR SATISFIED CLIENTS</h2>
  <p class="lead">Our commitment to excellence has earned us the trust of numerous homeowners and businesses in London. Read their stories and understand the Torvin Group difference.</p>
  <span class="arrow" style="left:40px">&#10094;</span>
  <span class="arrow" style="right:40px">&#10095;</span>
  <div class="cards">
    <div class="card">
      <div class="avatar" role="img" aria-label="Client portrait"></div>
      <div>
        <p>Great team from start to finish. The extension was delivered on time, tidy and built with real care for detail.</p>
        <div class="name">Liam Carter</div>
        <div class="stars">&#9733;&#9733;&#9733;&#9733;&#9733;</div>
      </div>
    </div>
    <div class="card">
      <div class="avatar" role="img" aria-label="Client portrait"></div>
      <div>
        <p>Our new kitchen looks superb. Clear pricing, friendly crew and finishes that feel built to last for years.</p>
        <div class="name">Liam Carter</div>
        <div class="stars">&#9733;&#9733;&#9733;&#9733;&#9733;</div>
      </div>
    </div>
  </div>
</section>

<section class="cta" role="img" aria-label="Warm copper toned construction site backdrop">
  <h2>READY TO START YOUR PROJECT?</h2>
  <p>Contact us today for a consultation and embark on the journey to turn your construction dreams into a stunning reality.</p>
  <a class="btn" href="#">CONTACT US &#10140;</a>
</section>

<footer class="footer">
  <div class="about">
    <div class="logo"><span class="mark"></span><span class="brand">TORVIN</span></div>
    <div class="social"><span class="dot"></span><span class="dot"></span><span class="dot"></span><span class="dot"></span></div>
  </div>
  <div class="col">
    <h4>Quick Links</h4>
    <ul><li>About Us</li><li>Services</li><li>Projects</li><li>Contact Us</li></ul>
  </div>
  <div class="col">
    <h4>About Company</h4>
    <ul><li>Support</li><li>Terms &amp; Condition</li><li>Contact Us</li><li>Privacy Policy</li><li>FAQ</li></ul>
  </div>
  <div class="col">
    <h4>Contact Us</h4>
    <div class="contact-item"><span>&#9742;</span><div><b>Phone</b>(020) 555-0148</div></div>
    <div class="contact-item"><span>&#9993;</span><div><b>Email</b>info@torvingroup.com</div></div>
    <div class="contact-item"><span>&#9679;</span><div><b>Location</b>48 Harbour Lane, London SE1 7PB</div></div>
  </div>
  <div class="to-top">&#8593;</div>
  <div class="copyright">2024 Copyright - Torvin Group. | All Rights Reserved.</div>
</footer>

</body>
</html>
```